Refresh old packing for HGH product

At now product has design like on photo.
Target is to make new one based on this. New one should be more medical, and luxury looks.

Colors
0054AA
0677BA
7BADD7
CADEEF
E8F1F8

```html
<!DOCTYPE html>
<html lang="en">
<head>
<meta charset="utf-8">
<title>Somatropin Carton – Front Panel</title>
<link rel="stylesheet" href="https://fonts.googleapis.com/css2?family=Montserrat:wght@500;600;700;900&display=swap">
<style>
  :root {
    --backdrop: #d3e2ea;
    --panel: #ffffff;
    --panel-shade: #eef3f7;
    --band: #2bb3e6;
    --band-deep: #1a9fdc;
    --title-blue: #1b9ae6;
    --navy: #1d3550;
    --ink: #1a1f26;
    --dna-light: #cadeef;
    --dna-mid: #7badd7;
    --wash: #e8f1f8;
  }
  * { margin: 0; padding: 0; box-sizing: border-box; }
  html, body {
    width: 1200px;
    height: 840px;
    overflow: hidden;
    background: var(--backdrop);
    font-family: "Montserrat", sans-serif;
  }
  .carton-front {
    position: absolute;
    left: 100px;
    top: 100px;
    width: 1000px;
    height: 640px;
    background: linear-gradient(135deg, var(--panel) 0%, var(--panel) 45%, var(--panel-shade) 100%);
    overflow: hidden;
  }
  .brand-band {
    position: absolute;
    left: 0;
    top: 0;
    width: 1000px;
    height: 140px;
  }
  .brand-lockup {
    position: absolute;
    left: 34px;
    top: 34px;
    display: flex;
    align-items: center;
    gap: 16px;
  }
  .brand-dot {
    width: 58px;
    height: 58px;
    border-radius: 50%;
    background: var(--panel);
    opacity: 0.9;
  }
  .brand-name {
    color: var(--panel);
    font-weight: 600;
    font-size: 22px;
    line-height: 1.1;
    letter-spacing: 1px;
    text-transform: uppercase;
  }
  .pack-count {
    position: absolute;
    right: 36px;
    top: 24px;
    font-size: 11px;
    font-weight: 500;
    color: var(--ink);
    letter-spacing: 0.3px;
  }
  .dna-art {
    position: absolute;
    left: 560px;
    top: 40px;
    width: 340px;
    height: 600px;
    border-radius: 160px;
    background: radial-gradient(ellipse at 50% 45%, var(--dna-mid) 0%, var(--dna-light) 45%, rgba(232,241,248,0) 75%);
    opacity: 0.55;
  }
  .emblem-art {
    position: absolute;
    left: 120px;
    top: 250px;
    width: 130px;
    height: 160px;
    border-radius: 50% 50% 40% 40%;
    background: linear-gradient(180deg, var(--title-blue) 0%, var(--dna-mid) 55%, var(--navy) 100%);
    opacity: 0.75;
  }
  .product-name {
    position: absolute;
    left: 262px;
    top: 238px;
    font-weight: 900;
    font-size: 90px;
    color: var(--title-blue);
    letter-spacing: 1px;
    line-height: 1;
  }
  .product-descriptor {
    position: absolute;
    left: 268px;
    top: 344px;
    font-weight: 700;
    font-size: 25px;
    color: var(--navy);
    letter-spacing: 0.5px;
  }
  .storage-note {
    position: absolute;
    right: 40px;
    top: 420px;
    text-align: right;
    font-weight: 600;
    font-size: 15px;
    line-height: 1.35;
    color: var(--ink);
  }
  .diluent-note {
    position: absolute;
    left: 40px;
    bottom: 40px;
    font-weight: 600;
    font-size: 19px;
    color: var(--ink);
    letter-spacing: 0.5px;
  }
</style>
</head>
<body>
  <section class="carton-front">
    <svg class="brand-band" viewBox="0 0 1000 140" aria-hidden="true">
      <path d="M0 0 H470 C420 0 405 40 395 80 C385 120 360 140 320 140 H0 Z" fill="var(--band)"/>
    </svg>
    <div class="brand-lockup">
      <span class="brand-dot"></span>
      <span class="brand-name">Kelvar<br>Laboratories</span>
    </div>
    <p class="pack-count">100IU BOX - 10 VIAL X 10IU (3.33MG)</p>

    <div class="dna-art" role="img" aria-label="Soft blue double helix illustration"></div>
    <div class="emblem-art" role="img" aria-label="Winged staff with serpent emblem"></div>

    <h1 class="product-name">SOMATROPIN</h1>
    <p class="product-descriptor">SOMATROPIN (RDNA ORIGIN) FOR INJECTION</p>

    <p class="storage-note">STORE BETWEEN 2-8<br>PROTECT FROM LIGHT.<br>DO NOT SHAKE</p>
    <p class="diluent-note">1 VIAL X 10ML STERILE DILUTENT</p>
  </section>
</body>
</html>
```